Redesign My Travel Voucher Coupons-Please redesign the flyers I have attached to this brief.

These designs will be catered towards like travel agency vacation stays...luxury resort stays, hotel and airfare getaways, etc. so must have a travel theme but more importantly professional trustworthy appeal...

Please redesign the flyers I have attached to this brief.

I have attached my existing designs. Please use all existing content and elements exactly but make the design much better...also, please keep in mind that these would be full color and printer friendly...

Target Market(s)

Consumers. People receive these vouchers from businesses that run marketing promotions and contests and giveaways. So the look and feel must feel professional and trustworthy but not cheesy and fake.

Industry/Entity Type

Hotel

Requirements
Must have
• Please use all existing content and elements exactly but make the design much better...also, please keep in mind that these would be full color and printer friendly...

MUST HAVE ALL EXISTING CONTENT EXACT NO EXCEPTIONS
Nice to have
• These designs will be catered towards like travel agency vacation stays...luxury resort stays, hotel and airfare getaways, etc. so must have a travel theme but more importantly professional trustworthy appeal...

Should not have

```html
<!DOCTYPE html>
<html lang="en">
<head>
<meta charset="utf-8">
<title>Luxury Cruise Travel Voucher</title>
<link rel="stylesheet" href="https://fonts.googleapis.com/css2?family=Bebas+Neue&family=Oswald:wght@300;500&family=Montserrat:wght@700;800&family=Arimo:wght@400;700&display=swap">
<style>
  :root{
    --red:#d8262c;
    --red-dark:#b51b21;
    --ink:#2b2b2b;
    --body:#333;
    --grey:#8a8a8a;
    --silver:#b9b9b9;
    --paper:#f4f4f4;
    --backdrop:#000;
  }
  *{margin:0;padding:0;box-sizing:border-box}
  html,body{width:974px;height:1200px;overflow:hidden;background:var(--backdrop)}
  .canvas{position:relative;width:974px;height:1200px;background:var(--backdrop)}
  .voucher{position:absolute;left:91px;top:89px;width:791px;height:1022px;overflow:hidden;
    background:linear-gradient(180deg,#ececec 0%,var(--paper) 45%,#fff 100%);
    font-family:"Arimo",Arial,sans-serif;color:var(--body)}
  .abs{position:absolute}
  .hero-art{position:absolute;left:0;top:0}
  .headline-enjoy{left:26px;top:12px;font-family:"Bebas Neue",sans-serif;font-size:140px;line-height:1;color:var(--red);letter-spacing:-1px}
  .headline-nights{left:262px;top:86px;font-family:"Oswald",sans-serif;font-weight:300;font-size:43px;line-height:1;color:var(--ink);letter-spacing:-0.5px}
  .ribbon{left:28px;top:128px;width:502px;height:50px;background:linear-gradient(180deg,#ee3a3f,var(--red-dark));
    clip-path:polygon(0 0,93% 0,100% 100%,0 100%)}
  .ribbon span{position:absolute;left:14px;top:3px;font-family:"Montserrat",sans-serif;font-weight:800;font-size:45px;line-height:1;color:#fff;letter-spacing:-0.5px}
  .subhead{left:29px;top:182px;font-family:"Montserrat",sans-serif;font-weight:700;font-size:25px;color:var(--ink);letter-spacing:-0.2px}
  .subhead em{font-style:normal;color:var(--red)}
  .compliments{left:599px;top:1px;width:157px;height:120px;background:#fff;text-align:center;color:var(--ink)}
  .compliments .label{margin-top:28px;font-family:"Montserrat",sans-serif;font-weight:700;font-size:9px;color:var(--red)}
  .compliments .brand{margin-top:8px;display:flex;align-items:center;justify-content:center;gap:5px;font-family:"Arimo",sans-serif;font-weight:700;font-size:9.5px;color:#1f6fb8}
  .compliments .brand i{display:block;width:9px;height:9px;border-radius:50%;background:#1f6fb8}
  .compliments .rep{margin-top:9px;font-size:12px;line-height:14px}
  .compliments .web{font-size:8.8px;line-height:14px}
  .tag{height:24px;background:linear-gradient(180deg,#ee3a3f,var(--red-dark));clip-path:polygon(0 0,86% 0,100% 100%,0 100%);
    font-family:"Oswald",sans-serif;font-weight:500;font-size:18px;line-height:24px;color:#fff;padding-left:10px;letter-spacing:-0.2px}
  .copy{font-size:10.4px;line-height:12.2px;text-align:justify;color:var(--body)}
  .divider{left:362px;top:487px;width:1px;height:396px;background:#777}
  .feature{display:flex;align-items:flex-start;gap:10px;font-size:12px;line-height:15.3px;color:var(--ink)}
  .feature svg{flex:none;width:34px;height:34px;margin-top:-2px}
  .feature svg *{fill:none;stroke:#555;stroke-width:1.6;stroke-linecap:round;stroke-linejoin:round}
  .quote{left:375px;top:816px;width:380px;font-size:10.4px;line-height:14px;color:var(--ink);padding-left:18px}
  .quote .mark-open{position:absolute;left:0;top:-3px;font-weight:700;font-size:26px;line-height:1;color:var(--grey)}
  .quote .mark-close{position:relative;top:7px;margin-left:3px;font-weight:700;font-size:22px;line-height:0;color:var(--grey)}
  .attrib{left:610px;top:870px;width:132px;text-align:right;font-size:10.4px;color:var(--ink)}
  .coupon{left:29px;top:902px;width:732px;height:93px;border:2px dashed var(--red);border-radius:10px}
  .coupon .split{position:absolute;left:180px;top:4px;bottom:4px;border-left:2px dashed var(--red)}
  .cert{position:absolute;left:0;width:180px;text-align:center;color:var(--ink)}
  .cert .k{font-size:11.5px;line-height:14px}
  .cert .v{font-size:17px;line-height:19px;color:var(--red)}
  .cert hr{width:86px;margin:4px auto 5px;border:0;border-top:1px solid #aaa}
  .redeem{position:absolute;left:182px;right:0;text-align:center;color:var(--ink)}
  .redeem .lead{margin-top:8px;font-size:14.4px;line-height:17.5px;letter-spacing:0.1px}
  .redeem .url{margin-top:5px;font-size:20.5px;line-height:22px;letter-spacing:3.2px;color:var(--red)}
  .redeem .fine{margin-top:5px;font-size:8.6px;line-height:10px}
</style>
</head>
<body>
<div class="canvas">
  <section class="voucher">

    <svg class="hero-art" width="791" height="1022" viewBox="0 0 791 1022">
      <defs>
        <linearGradient id="heroSky" x1="0" y1="0" x2="0" y2="1">
          <stop offset="0" stop-color="#38a6e6"/>
          <stop offset="0.42" stop-color="#c5e6f6"/>
          <stop offset="0.62" stop-color="#5fd0d8"/>
          <stop offset="0.78" stop-color="#9fdfd8"/>
          <stop offset="1" stop-color="#e6dac3"/>
        </linearGradient>
        <radialGradient id="heroPalms" cx="0.92" cy="0.55" r="0.4">
          <stop offset="0" stop-color="#5b8f2c" stop-opacity="0.95"/>
          <stop offset="0.6" stop-color="#8bb04a" stop-opacity="0.6"/>
          <stop offset="1" stop-color="#8bb04a" stop-opacity="0"/>
        </radialGradient>
        <linearGradient id="houseTone" x1="0" y1="0" x2="0" y2="1">
          <stop offset="0" stop-color="#3f9de3"/><stop offset="0.55" stop-color="#d0609a"/><stop offset="1" stop-color="#efe7d6"/>
        </linearGradient>
        <linearGradient id="palmTone" x1="0" y1="0" x2="0" y2="1">
          <stop offset="0" stop-color="#5aa8e0"/><stop offset="0.55" stop-color="#9fd6ea"/><stop offset="1" stop-color="#f0ece4"/>
        </linearGradient>
        <linearGradient id="deckTone" x1="0" y1="0" x2="0" y2="1">
          <stop offset="0" stop-color="#f0b84a"/><stop offset="0.5" stop-color="#c79a6a"/><stop offset="1" stop-color="#2f6b78"/>
        </linearGradient>
      </defs>

      <g role="img" aria-label="Cruise ship docked beside a tropical beach with swimmers, lounge chairs and palm trees">
        <path d="M0 0H791V398C735 418 695 385 676 335C650 262 565 250 500 292C420 345 330 470 190 467C100 465 40 430 0 380Z" fill="url(#heroSky)"/>
        <path d="M520 0H791V398C735 418 695 385 676 335C650 262 590 250 540 270Z" fill="url(#heroPalms)"/>
      </g>
      <path d="M0 380C40 430 100 465 190 467C330 470 420 345 500 292C565 250 650 262 676 335C695 385 735 418 791 398"
            fill="none" stroke="#9a9a9a" stroke-width="7"/>

      <circle cx="569" cy="389" r="98" fill="#fff" stroke="var(--silver)" stroke-width="6"/>
      <circle cx="569" cy="389" r="90" fill="url(#houseTone)" role="img" aria-label="Colourful stilt beach house on white sand with blue lounge chairs"/>

      <circle cx="504" cy="555" r="76" fill="#fff" stroke="var(--silver)" stroke-width="6"/>
      <circle cx="504" cy="555" r="68" fill="url(#palmTone)" role="img" aria-label="Palm trees on a white sand beach"/>

      <circle cx="669" cy="545" r="84" fill="#fff" stroke="var(--silver)" stroke-width="6"/>
      <circle cx="669" cy="545" r="76" fill="url(#deckTone)" role="img" aria-label="Cruise ship pool deck at sunset"/>
    </svg>

    <div class="abs headline-enjoy">ENJOY</div>
    <div class="abs headline-nights">A 4 NIGHT</div>
    <div class="abs ribbon"><span>LUXURY CRUISE</span></div>
    <div class="abs subhead"><em>7 Nights Luxury</em> Resort Getaway</div>

    <aside class="abs compliments">
      <div class="label">Compliments Of</div>
      <div class="brand"><i></i>BRIGHT PATH INCENTIVES</div>
      <div class="rep">Dana Mercer<br>555-014-2290</div>
      <div class="web">www.GrowYourClientele.com</div>
    </aside>

    <div class="abs tag" style="left:28px;top:487px;width:160px">EXCLUSIVELY FOR:</div>
    <p class="abs copy" style="left:39px;top:516px;width:305px">Congratulations, you are the lucky recipient of a 5 day /4 night Cruise aboard choice of: Coral Star Cruise Lines, Royal Horizon, Northwind Cruise Lines, or Duchess Cruises. There are 3 itineraries w/ ports of departure including: Miami to Cozumel, Port Canaveral to Nassau, or LA to Ensenada, Mexico. All cruises include unlimited access to the on-board buffets for breakfast, lunch and dinner. Vegas style entertainment and use of all on-board facilities. You simply pay taxes and port fees. Have the time of your life while enjoying the luxuries of a cruise vacation!</p>

    <div class="abs tag" style="left:28px;top:632px;width:160px">FEATURES</div>

    <div class="abs feature" style="left:28px;top:673px;width:160px">
      <svg viewBox="0 0 34 34"><rect x="3" y="3" width="14" height="26" rx="2"/><rect x="6" y="7" width="8" height="5"/><path d="M6 16h2M10 16h2M6 20h2M10 20h2M6 24h2M10 24h2"/><circle cx="26" cy="25" r="7"/><path d="M23 28v-5h6v5M25 24v1M27 24v1"/></svg>
      <span>Phone Bookings<br>With A Live Agent</span>
    </div>
    <div class="abs feature" style="left:28px;top:730px;width:160px">
      <svg viewBox="0 0 34 34"><path d="M4 9c4-4 22-4 26 0"/><path d="M17 5v5"/><rect x="5" y="12" width="24" height="18" rx="2"/><path d="M12 12V9h10v3"/><path d="M12 25l10-8M13 19l3 3M18 23l3 3"/></svg>
      <span>Redeem Now,<br>Travel Later</span>
    </div>
    <div class="abs feature" style="left:28px;top:778px;width:170px">
      <svg viewBox="0 0 34 34"><path d="M17 2l3 4 5-1 1 5 5 2-2 5 2 5-5 2-1 5-5-1-3 4-3-4-5 1-1-5-5-2 2-5-2-5 5-2 1-5 5 1z" style="fill:#555;stroke:#555"/><circle cx="17" cy="17" r="8" style="stroke:#fff"/><path d="M13 17l3 3 5-6" style="stroke:#fff"/></svg>
      <span>No Timeshare Or<br>Sales Presentation<br>Guaranteed!</span>
    </div>
    <div class="abs feature" style="left:28px;top:841px;width:170px">
      <svg viewBox="0 0 34 34"><path d="M8 5h20M24 1l4 4-4 4"/><path d="M26 29H6M10 25l-4 4 4 4"/><circle cx="10" cy="17" r="6"/><circle cx="24" cy="17" r="6"/><circle cx="10" cy="15" r="2"/><circle cx="24" cy="15" r="2"/></svg>
      <span>Fully Transferable<br>To Another Person</span>
    </div>

    <div class="abs feature" style="left:195px;top:673px;width:160px">
      <svg viewBox="0 0 34 34"><path d="M16 3v21M16 4l9 4-9 3" style="fill:#555"/><path d="M15 7L6 22h9z" style="fill:#555"/><path d="M4 25h26l-3 4H7z" style="fill:#555"/><path d="M3 32c3-2 5 2 8 0s5 2 8 0 5 2 8 0 4 1 5 0"/></svg>
      <span>Sailing From: Miami,<br>Port Canaveral or<br>Los Angeles</span>
    </div>
    <div class="abs feature" style="left:195px;top:730px;width:160px">
      <svg viewBox="0 0 34 34"><path d="M7 2h14l7 7v23H7z" style="fill:#555"/><path d="M13 8c-3 0-3 4 0 4s3 4 0 4M13 6v12M17 14h7M17 19h7M11 23h13M11 27h13" style="stroke:#fff"/></svg>
      <span>Pay Just<br>The Taxes &amp; Fees</span>
    </div>
    <div class="abs feature" style="left:195px;top:778px;width:160px">
      <svg viewBox="0 0 34 34"><path d="M17 2v22"/><path d="M16 5L6 22h10zM18 8l8 14h-8z"/><path d="M3 25h28l-4 6H7z"/><path d="M10 28h2M16 28h2M22 28h2"/></svg>
      <span>Sail To: Cozumel,<br>Nassau Bahamas<br>or Ensenada</span>
    </div>
    <div class="abs feature" style="left:195px;top:841px;width:165px">
      <svg viewBox="0 0 34 34"><rect x="3" y="6" width="28" height="26" rx="2"/><path d="M3 12h28M9 3v6M15 3v6M21 3v6M27 3v6"/><path d="M10 28l5-4 4-8 2 1-2 8 6 3-1 2-7-2-5 2"/></svg>
      <span>You Will Have 24<br>Months To Complete<br>Travel Offer</span>
    </div>

    <div class="abs divider"></div>

    <div class="abs tag" style="left:375px;top:655px;width:182px">HOW CAN WE DO THIS?</div>
    <p class="abs copy" style="left:384px;top:688px;width:378px;line-height:13.4px">We contract with world leading cruise lines to help them fill their otherwise empty rooms. The cruise lines now gain a new customer for their in-house restaurants, room service, the casino, spa and even future bookings. They know that if they show you a good time, you will probably tell your friends and family about the great time you had and may even book with them on a future cruise, but this time as a regular paying customer.</p>

    <div class="abs tag" style="left:375px;top:782px;width:157px">WHAT OTHERS SAY</div>
    <p class="abs quote"><span class="mark-open">&ldquo;</span>The food was delicious in the buffet and the restaurant that was included in our ticket had delicious appetizers, entrees and desserts to choose from. The room was very clean and everything worked fine.<span class="mark-close">&rdquo;</span></p>
    <p class="abs attrib">Marisol T.&nbsp; New York, NY</p>

    <div class="abs coupon">
      <div class="split"></div>
      <div class="cert" style="top:10px">
        <div class="k">Certificate ID</div>
        <div class="v">107083-11269</div>
        <hr>
        <div class="k">Expires</div>
        <div class="v">11/07/2020</div>
      </div>
      <div class="redeem">
        <div class="lead">VIEW ALL THE DETAILS OF THIS SPECIAL OFFER<br>AND REDEEM ONLINE AT</div>
        <div class="url">WWW.TRAVELPERKSONLINE.COM</div>
        <div class="fine">*Terms and Conditions apply see website for details</div>
      </div>
    </div>

  </section>
</div>
</body>
</html>
```